依頼詳細
爽やかさ、リゾート感、海などを感じられるようなデザインを希望しています。
ロゴマークは、指定のものがありますので
このロゴマークを名刺のデザインに加えてください。
ロゴマークは青ですが、色の変更をしていただいても構いません。
ちなみに、このロゴは、サーフボード、朝陽、水平線などをイメージしています。
その他のイメージ等は、ホームページをご覧になって、
何かを感じていただけたらと思います。
http://www.tomika-vel.com
記載項目
ロゴマーク、屋号、住所・TEL/FAX(ホノルル&福岡の2か所)
スタッフ名 肩書、携帯番号、メールアドレス、URLを記載
名刺デザインは、両面を使ってください。
どちらの面に何を記載するかは、お任せいたします。
希望イメージ
シンプル 複雑
単色 カラフル
暗い 明るい
日常 高級
遊び心 厳粛
未来的 伝統的
女性的 男性的
希望する色
青系、黄・オレンジ系、グレー系
納品ファイル
• 高解像度JPG (.jpg)
• イラストレーター形式 (.ai)
• フォトショップ形式 (.psd)
• PNG形式 (.png)
補足説明
記載事項は、屋号にある「夢」以外は、すべてローマ字記載の予定です。

ちなみに携帯電話は→Personal Phoneと記載してください。
URL http://www.tomika-vel.com
E-mail kanda@tomika-vel.com

記載事項が多いので、例えばですが

表面を屋号と個人情報
裏面をショップ情報
に分ける等、できるだけ見やすく仕上げてください。

もちろん、この記載事項の分け方にこだわりはありませんので
デザイン上柔軟にご対応願います。

よろしくお願いいたします。

```html
<!DOCTYPE html>
<html lang="en">
<head>
<meta charset="utf-8">
<title>TOMIKAVEL Holdings — Business Card Back</title>
<link href="https://fonts.googleapis.com/css2?family=EB+Garamond:wght@500&family=Roboto:wght@400&display=swap" rel="stylesheet">
<style>
  :root {
    --card-blue: #123f8b;
    --text-light: #eef2f8;
    --text-soft: #dde5f2;
  }
  html, body {
    margin: 0;
    padding: 0;
    width: 1200px;
    height: 729px;
    overflow: hidden;
    background: var(--card-blue);
  }
  .card {
    position: relative;
    width: 1200px;
    height: 729px;
    background: var(--card-blue);
    color: var(--text-light);
  }
  .office {
    position: absolute;
    left: 163px;
  }
  .office--main { top: 176px; }
  .office--satellite { top: 403px; }
  .office__name {
    margin: 0 0 24px;
    font-family: "EB Garamond", serif;
    font-weight: 500;
    font-size: 38px;
    line-height: 1.1;
    letter-spacing: 0.3px;
  }
  .office__line {
    margin: 0;
    font-family: "Roboto", Arial, sans-serif;
    font-size: 23px;
    line-height: 42px;
    color: var(--text-soft);
    letter-spacing: 0.2px;
  }
</style>
</head>
<body>
  <div class="card">
    <section class="office office--main">
      <h1 class="office__name">TOMIKAVEL Holdings</h1>
      <p class="office__line">415 Coral Lane, Honolulu, HI 96815 U.S.A.</p>
      <p class="office__line">Phone +1-808-555-0142 Fax+1-808-555-0143</p>
    </section>
    <section class="office office--satellite">
      <h2 class="office__name">Satellite Office</h2>
      <p class="office__line">Level 12, 2-4-8 Minato, Chuo-ku, Fukuoka 810-0002 Japan</p>
      <p class="office__line">Phone +81-92-555-0186 Fax+81-92-555-0187</p>
    </section>
  </div>
</body>
</html>
```